IT Company based on Biology Business Needs a PowerPoint Design

We need a powerpoint design for a new company called 'Vast KELP'. We develop the machine learning solutions especially focused on deep learning algorithms for biology industry. Our initial product is a vision detection on biological images to help doctors diagnose the symptoms. We would like to see designs that use the color green.

Industry/Entity Type

Biotechnology

Requirements
Nice to have
• Lots of slide templates with company logo's look and feel

```html
<!DOCTYPE html>
<html lang="en">
<head>
<meta charset="utf-8">
<title>Vast KELP — Presentation Templates</title>
<link rel="stylesheet" href="https://fonts.googleapis.com/css2?family=Roboto:wght@300;400;500;700&display=swap">
<style>
:root{
  --bg:#d3d3d5;
  --green:#6cbf3e;
  --green-mid:#3fa43a;
  --green-dark:#1c7f36;
  --green-deep:#12672c;
  --gray:#8e8e8e;
  --gray-light:#c9c9c9;
  --ink:#5a5a5a;
  --title:#4d7f3c;
  --white:#ffffff;
}
*{box-sizing:border-box}
html,body{margin:0;padding:0}
body{width:1200px;height:900px;overflow:hidden;background:var(--bg);font-family:'Roboto',sans-serif;color:var(--ink)}
.deck{position:absolute;left:138px;top:27px;display:grid;grid-template-columns:repeat(3,289px);grid-auto-rows:163px;gap:6px 5px}
.slide{position:relative;background:var(--white);overflow:hidden}
.abs{position:absolute}
.slide-title{position:absolute;left:10px;right:10px;top:9px;font-size:7px;font-weight:300;color:var(--title);text-transform:uppercase;border-bottom:.6px solid #bdbdbd;padding-bottom:1px;letter-spacing:.1px}
.foot{position:absolute;left:0;right:0;bottom:0;height:3px;background:#a8a8a8}
.foot::after{content:"";position:absolute;right:0;top:0;bottom:0;width:9%;background:var(--green)}
.mini-logo{position:absolute;left:4px;bottom:6px;display:flex;align-items:center;gap:1.5px;font-size:4px;font-weight:500;color:var(--green-mid)}
.mini-logo i{display:block;width:3px;height:3px;border-radius:50%;background:var(--green-mid)}
.tiny{font-size:3.2px;line-height:4.2px;color:#7a7a7a;text-align:justify}
.tiny.center{text-align:center}
.img-fill{position:absolute}

/* cover */
.cover-band{left:0;top:39px;width:289px;height:78px;background:linear-gradient(100deg,#3e9a2c 0%,#5fb83a 45%,#7cc743 100%)}
.cover-photo{left:0;top:39px;width:170px;height:78px;background:radial-gradient(ellipse at 30% 40%,#a7e06a 0%,#5bb337 45%,rgba(70,160,45,0) 80%)}
.cover-strip{left:0;top:117px;width:289px;height:6px;background:linear-gradient(90deg,#9a9a9a,#c9c9c9)}
.cover-welcome{right:12px;top:60px;text-align:right;color:var(--white)}
.cover-welcome h1{margin:0;font-size:11px;font-weight:500;letter-spacing:.3px}
.cover-welcome p{margin:1px 0 0;font-size:7px;font-weight:300;letter-spacing:2px}
.cover-welcome small{display:block;margin-top:2px;font-size:3.4px}
.brand{display:flex;align-items:center;gap:3px;color:var(--green-mid);font-weight:400}
.brand i{display:block;border-radius:50%;background:var(--green-mid)}

/* contents */
.contents-bg{inset:0;background:radial-gradient(ellipse at 80% 60%,#2ea444 0%,#17843a 45%,#0f6a2e 100%)}
.contents-head{left:29px;top:47px;color:var(--white)}
.contents-head small{display:block;font-size:3.6px;letter-spacing:.3px}
.contents-head h2{margin:0;font-size:10px;font-weight:300;border-bottom:1px solid var(--white);display:inline-block;padding-bottom:1px}
.toc-row{position:absolute;left:131px;width:123px;height:9px;background:#e9e9e9;border-radius:1px;font-size:4px;line-height:9px;color:#555;padding-left:17px}
.toc-row b{position:absolute;left:2px;top:0;width:9px;height:9px;border-radius:50%;background:var(--green);border:1px solid var(--white);color:var(--white);font-size:4px;line-height:7px;text-align:center;font-weight:500}

/* about 1 */
.about-box{left:0;top:46px;width:94px;height:52px;background:var(--green);color:var(--white);font-size:3.6px;line-height:4.8px;padding:16px 10px 0 17px}
.about-photo{left:94px;top:46px;width:195px;height:52px;background:linear-gradient(90deg,#e9eef2,#c7d3dc 50%,#edf1f4)}

/* about grid */
.cell{position:absolute;height:36px;font-size:3.3px;line-height:4.3px;color:var(--white);padding:4px 6px}
.cell.green{background:var(--green);display:flex;align-items:center;justify-content:center;font-size:4px}
.cell.gray{background:#8a8a8a}
.cell.photo{background:linear-gradient(135deg,#f2f2f2,#d9dee2)}

/* market */
.market-label{position:absolute;font-weight:700;color:var(--green)}
/* chart */
.legend{position:absolute;top:125px;font-size:3px;color:#777;width:60px}
.legend b{display:inline-block;width:3px;height:3px;margin-right:2px;vertical-align:middle}

/* services */
.service{position:absolute;top:45px;width:59px;height:92px}
.service .top{height:37px;display:flex;align-items:center;justify-content:center}
.service .bottom{height:55px;background:#8d8d8d;color:var(--white);padding:5px 5px;font-size:3.2px;line-height:4.2px;text-align:center}

/* team */
.member{position:absolute;top:42px;width:70px;text-align:center}
.member .avatar{width:34px;height:34px;margin:0 auto;border-radius:50%;border:1.5px solid var(--green);background:linear-gradient(160deg,#e2e2e2,#a8a8a8)}
.member h4{margin:4px 0 0;font-size:3.6px;font-weight:500;color:var(--green-mid)}
.member small{display:block;font-size:2.8px;color:#888;margin-bottom:3px}

/* table */
.data-table{position:absolute;left:63px;top:50px;width:160px;border-collapse:collapse;font-size:2.8px;color:#333}
.data-table caption{background:var(--green);color:var(--white);text-align:left;font-weight:700;font-size:3.8px;padding:1px 2px}
.data-table td{padding:0 2px;height:5.7px;border-bottom:.4px solid #cfcfcf}
.data-table tr:nth-child(even) td{background:#eef6e9}
.data-table td.num{text-align:right}
.data-table tr.total td{font-weight:700;background:#fff;border-bottom:none}

/* partners */
.partner-box{left:61px;top:40px;width:173px;height:96px;background:var(--white);border:.6px solid #ddd;box-shadow:0 2px 3px rgba(0,0,0,.12);display:grid;grid-template-columns:repeat(4,1fr);grid-template-rows:repeat(4,1fr);place-items:center;padding:6px 8px}
.badge{width:30px;height:9px;border-radius:1px}

/* image text */
.imgtext-panel{left:0;top:0;width:125px;height:163px;background:var(--green);color:var(--white);padding:16px 18px}
.imgtext-panel h3{margin:0 0 44px;font-size:7px;font-weight:300}
.imgtext-panel .tiny{color:var(--white)}
.imgtext-photo{left:125px;top:0;width:164px;height:163px;background:linear-gradient(110deg,#eef4f8 0%,#8fc6e8 40%,#2b7fc4 65%,#dce9f2 100%)}

/* section */
.section-bg{inset:0;background:radial-gradient(circle at 30% 40%,#8fd04d 0%,#5cb332 45%,#3c9425 100%)}
.section-mark{left:127px;top:62px;width:34px;height:34px;border-radius:50%;background:var(--white);color:var(--green-mid);font:italic 700 22px/34px Georgia,serif;text-align:center}
.section-rule{left:94px;top:107px;width:100px;height:.6px;background:var(--white)}
.section-title{left:0;right:0;top:111px;text-align:center;color:var(--white);font-size:8px;font-weight:300}

/* contact */
.contact-top{left:0;top:0;width:289px;height:3px;background:var(--green-dark)}
.contact-map{left:0;top:65px;width:289px;height:73px;background:linear-gradient(180deg,#e6e6e2 0%,#d8ddd3 50%,#b3cfe0 100%)}
.contact-bar{left:0;top:138px;width:289px;height:25px;background:var(--green-dark);display:flex;align-items:center;justify-content:space-around;padding:0 18px;font-size:4px;color:var(--white)}
.contact-bar span{display:flex;align-items:center;gap:2px}
.contact-bar i{display:block;width:5px;height:5px;border-radius:50%;background:var(--green)}
</style>
</head>
<body>
<main class="deck">

  <!-- Cover -->
  <section class="slide">
    <div class="abs cover-band"></div>
    <div class="img-fill cover-photo" role="img" aria-label="Green glowing DNA helix"></div>
    <div class="abs cover-strip"></div>
    <div class="abs cover-welcome">
      <h1>WELCOME</h1>
      <p>TO OUR PRESENTATION</p>
      <small>Birmingham, March 25, 2011</small>
    </div>
    <div class="abs brand" style="left:204px;top:128px;font-size:12px"><i style="width:8px;height:8px"></i>Vast KELP</div>
  </section>

  <!-- Table of contents -->
  <section class="slide">
    <div class="img-fill contents-bg" role="img" aria-label="Dark green background with faint DNA strands"></div>
    <div class="abs contents-head"><small>TABLE OF</small><h2>CONTENTS</h2></div>
    <div class="toc-row" style="top:62px"><b>1</b>LOREM IPSUM DOLOR SIT MET</div>
    <div class="toc-row" style="top:77px"><b>2</b>LOREM IPSUM DOLOR SIT MET</div>
    <div class="toc-row" style="top:92px"><b>3</b>LOREM IPSUM DOLOR SIT MET</div>
    <div class="toc-row" style="top:107px"><b>4</b>LOREM IPSUM DOLOR SIT MET</div>
    <div class="toc-row" style="top:122px"><b>5</b>LOREM IPSUM DOLOR SIT MET</div>
    <div class="toc-row" style="top:137px"><b>6</b>LOREM IPSUM DOLOR SIT MET</div>
  </section>

  <!-- About us, team banner -->
  <section class="slide">
    <div class="slide-title">About us</div>
    <div class="abs about-box">LOREM IPSUM DOLOR SIT AMET CONSECTETUR ADIPISCING ELIT SED DO EIUSMOD TEMPOR INCIDIDUNT UT LABORE ET DOLORE MAGNA</div>
    <div class="img-fill about-photo" role="img" aria-label="Group of smiling medical staff in white coats"></div>
    <p class="abs tiny" style="left:90px;top:104px;width:184px;margin:0">Lorem ipsum dolor sit amet, consectetur adipiscing elit, sed do eiusmod tempor incididunt ut labore et dolore magna aliqua. Ut enim ad minim veniam, quis nostrud exercitation ullamco laboris nisi ut aliquip ex ea commodo consequat. Duis aute irure dolor in reprehenderit in voluptate velit esse cillum dolore eu fugiat nulla pariatur.</p>
    <div class="mini-logo"><i></i>Vast KELP</div>
    <div class="foot"></div>
  </section>

  <!-- About us, grid -->
  <section class="slide">
    <div class="slide-title">About us</div>
    <div class="cell green" style="left:24px;top:30px;width:63px">LOREM IPSUM DOLOR</div>
    <div class="cell photo" style="left:87px;top:30px;width:59px" role="img" aria-label="Doctor examining a child"></div>
    <div class="cell gray" style="left:146px;top:30px;width:122px">Lorem ipsum dolor sit amet, consectetur adipiscing elit, sed do eiusmod tempor incididunt ut labore et dolore magna aliqua. Ut enim ad minim veniam, quis nostrud exercitation.</div>
    <div class="cell gray" style="left:24px;top:66px;width:122px">Lorem ipsum dolor sit amet, consectetur adipiscing elit, sed do eiusmod tempor incididunt ut labore et dolore magna aliqua. Ut enim ad minim veniam, quis nostrud exercitation.</div>
    <div class="cell green" style="left:146px;top:66px;width:64px">LOREM IPSUM DOLOR</div>
    <div class="cell photo" style="left:210px;top:66px;width:58px" role="img" aria-label="Doctor talking with a patient"></div>
    <div class="cell photo" style="left:24px;top:102px;width:63px" role="img" aria-label="Nurse checking a patient's blood pressure"></div>
    <div class="cell green" style="left:87px;top:102px;width:59px">LOREM IPSUM DOLOR</div>
    <div class="cell gray" style="left:146px;top:102px;width:122px">Lorem ipsum dolor sit amet, consectetur adipiscing elit, sed do eiusmod tempor incididunt ut labore et dolore magna aliqua. Ut enim ad minim veniam, quis nostrud exercitation.</div>
    <div class="mini-logo"><i></i>Vast KELP</div>
    <div class="foot"></div>
  </section>

  <!-- About us, columns -->
  <section class="slide">
    <div class="slide-title">About us</div>
    <div class="img-fill" style="left:17px;top:42px;width:50px;height:34px;background:linear-gradient(135deg,#f4f4f4,#cfd6dc)" role="img" aria-label="Doctors reviewing notes at a desk"></div>
    <p class="abs tiny center" style="left:14px;top:79px;width:56px;margin:0;color:var(--green)">Lorem ipsum dolor sit amet consectetur adipiscing elit sed do eiusmod</p>
    <p class="abs tiny" style="left:78px;top:43px;width:90px;margin:0">Lorem ipsum dolor sit amet, consectetur adipiscing elit, sed do eiusmod tempor incididunt ut labore et dolore magna aliqua. Ut enim ad minim veniam, quis nostrud exercitation ullamco laboris nisi ut aliquip ex ea commodo consequat. Duis aute irure dolor in reprehenderit in voluptate velit esse cillum dolore eu fugiat nulla pariatur.</p>
    <p class="abs tiny" style="left:78px;top:100px;width:90px;margin:0">Lorem ipsum dolor sit amet, consectetur adipiscing elit, sed do eiusmod tempor incididunt ut labore et dolore magna aliqua. Ut enim ad minim veniam, quis nostrud exercitation ullamco laboris nisi ut aliquip ex ea commodo.</p>
    <p class="abs tiny" style="left:178px;top:43px;width:90px;margin:0">Lorem ipsum dolor sit amet, consectetur adipiscing elit, sed do eiusmod tempor incididunt ut labore et dolore magna aliqua. Ut enim ad minim veniam, quis nostrud exercitation ullamco laboris nisi ut aliquip ex ea commodo consequat. Duis aute irure dolor in reprehenderit in voluptate velit esse cillum dolore eu fugiat nulla pariatur.</p>
    <p class="abs tiny" style="left:178px;top:100px;width:90px;margin:0">Lorem ipsum dolor sit amet, consectetur adipiscing elit, sed do eiusmod tempor incididunt ut labore et dolore magna aliqua. Ut enim ad minim veniam, quis nostrud exercitation ullamco laboris nisi ut aliquip ex ea commodo.</p>
    <div class="mini-logo"><i></i>Vast KELP</div>
    <div class="foot"></div>
  </section>

  <!-- Market -->
  <section class="slide">
    <div class="slide-title">Our market</div>
    <svg class="abs" style="left:0;top:0" width="289" height="163" viewBox="0 0 289 163">
      <g fill="none" stroke-width="10">
        <circle cx="95" cy="89" r="37" stroke="var(--green)" stroke-dasharray="134.9 232.5" transform="rotate(-90 95 89)"/>
        <circle cx="95" cy="89" r="37" stroke="var(--green-dark)" stroke-dasharray="39.5 232.5" stroke-dashoffset="-134.9" transform="rotate(-90 95 89)"/>
        <circle cx="95" cy="89" r="37" stroke="#8c8c8c" stroke-dasharray="30.2 232.5" stroke-dashoffset="-174.4" transform="rotate(-90 95 89)"/>
        <circle cx="95" cy="89" r="37" stroke="#aee07f" stroke-dasharray="27.9 232.5" stroke-dashoffset="-204.6" transform="rotate(-90 95 89)"/>
      </g>
      <circle cx="95" cy="89" r="27" fill="#fff" stroke="var(--green)" stroke-width="1"/>
      <g fill="var(--green-dark)">
        <circle cx="95" cy="76" r="3"/>
        <rect x="90.5" y="80" width="9" height="11" rx="2"/>
        <rect x="91.5" y="90" width="3" height="12"/>
        <rect x="95.5" y="90" width="3" height="12"/>
      </g>
      <g stroke="#888" stroke-width=".5" fill="none">
        <polyline points="52,46 72,46 80,60"/>
        <polyline points="38,71 38,80 58,80"/>
        <polyline points="44,126 44,114 62,110"/>
        <polyline points="156,53 134,53 126,64"/>
      </g>
    </svg>
    <div class="market-label" style="left:34px;top:38px;font-size:7px;color:var(--green-dark)">17%</div>
    <div class="market-label" style="left:21px;top:67px;font-size:7px;color:#8c8c8c">13%</div>
    <div class="market-label" style="left:33px;top:126px;font-size:7px;color:var(--green-dark)">12%</div>
    <div class="market-label" style="left:159px;top:43px;font-size:11px">58%</div>
    <p class="abs tiny" style="left:170px;top:72px;width:104px;margin:0"><span style="color:var(--green)">Lorem ipsum dolor sit amet</span><br>consectetur adipiscing elit, sed do eiusmod tempor incididunt ut labore et dolore magna aliqua. Ut enim ad minim veniam, quis nostrud exercitation ullamco laboris nisi ut aliquip ex ea commodo consequat. Duis aute irure dolor in reprehenderit in voluptate velit esse cillum.</p>
    <div class="mini-logo"><i></i>Vast KELP</div>
    <div class="foot"></div>
  </section>

  <!-- Bar chart -->
  <section class="slide">
    <div class="slide-title">Our chart</div>
    <svg class="abs" style="left:0;top:0" width="289" height="163" viewBox="0 0 289 163">
      <g stroke="#999" stroke-width=".5">
        <line x1="63" y1="34" x2="63" y2="113"/>
        <line x1="60" y1="48" x2="63" y2="48"/><line x1="60" y1="64" x2="63" y2="64"/>
        <line x1="60" y1="80" x2="63" y2="80"/><line x1="60" y1="96" x2="63" y2="96"/>
      </g>
      <g>
        <rect x="69" y="56" width="8" height="57" fill="var(--green)"/>
        <rect x="79" y="82" width="8" height="31" fill="var(--green-mid)"/>
        <rect x="103" y="76" width="8" height="37" fill="var(--green)"/>
        <rect x="111" y="57" width="8" height="56" fill="#a9a9a9"/>
        <rect x="119" y="85" width="8" height="28" fill="var(--green-mid)"/>
        <rect x="136" y="62" width="8" height="51" fill="var(--green)"/>
        <rect x="144" y="87" width="8" height="26" fill="#a9a9a9"/>
        <rect x="152" y="76" width="8" height="37" fill="var(--green-mid)"/>
        <rect x="170" y="82" width="8" height="31" fill="#a9a9a9"/>
        <rect x="179" y="59" width="8" height="54" fill="var(--green-mid)"/>
        <rect x="110" y="48" width="9" height="4" fill="#a9a9a9"/>
        <rect x="135" y="54" width="9" height="4" fill="var(--green)"/>
        <rect x="151" y="68" width="9" height="4" fill="var(--green-mid)"/>
      </g>
      <g font-size="5" fill="#555" text-anchor="middle" font-family="Roboto, sans-serif">
        <text x="78" y="122">2009</text><text x="113" y="122">2010</text>
        <text x="146" y="122">2011</text><text x="180" y="122">2012</text>
      </g>
    </svg>
    <div class="legend" style="left:44px"><b style="background:var(--green)"></b>LOREM IPSUM<br>Lorem ipsum dolor sit amet consectetur adipiscing elit sed do</div>
    <div class="legend" style="left:107px"><b style="background:#a9a9a9"></b>LOREM IPSUM<br>Lorem ipsum dolor sit amet consectetur adipiscing elit sed do</div>
    <div class="legend" style="left:170px"><b style="background:var(--green-dark)"></b>LOREM IPSUM<br>Lorem ipsum dolor sit amet consectetur adipiscing elit sed do</div>
    <div class="mini-logo"><i></i>Vast KELP</div>
    <div class="foot"></div>
  </section>

  <!-- Ring chart -->
  <section class="slide">
    <div class="slide-title">Our chart</div>
    <svg class="abs" style="left:0;top:0" width="289" height="163" viewBox="0 0 289 163">
      <g fill="none" stroke-width="3.5">
        <circle cx="58" cy="73" r="17" stroke="#9c9c9c"/>
        <circle cx="58" cy="73" r="17" stroke="var(--green-mid)" stroke-dasharray="86.5 106.8" transform="rotate(-90 58 73)"/>
        <circle cx="142" cy="73" r="17" stroke="#9c9c9c"/>
        <circle cx="142" cy="73" r="17" stroke="var(--green-mid)" stroke-dasharray="76.9 106.8" transform="rotate(-90 142 73)"/>
        <circle cx="225" cy="73" r="17" stroke="#9c9c9c"/>
        <circle cx="225" cy="73" r="17" stroke="var(--green-mid)" stroke-dasharray="67.3 106.8" transform="rotate(-90 225 73)"/>
      </g>
      <g font-size="6" font-weight="700" fill="var(--green)" text-anchor="middle" font-family="Roboto, sans-serif">
        <text x="58" y="75">81%</text><text x="142" y="75">72%</text><text x="225" y="75">63%</text>
      </g>
    </svg>
    <p class="abs tiny center" style="left:28px;top:100px;width:60px;margin:0">dolor sit amet, consectetur adipiscing elit, sed do eiusmod tempor incididunt ut labore et dolore magna aliqua. Ut enim ad minim veniam, quis nostrud exercitation ullamco laboris nisi ut aliquip ex ea fugiat nulla pariatur.</p>
    <p class="abs tiny center" style="left:112px;top:100px;width:60px;margin:0">dolor sit amet, consectetur adipiscing elit, sed do eiusmod tempor incididunt ut labore et dolore magna aliqua. Ut enim ad minim veniam, quis nostrud exercitation ullamco laboris nisi ut aliquip ex ea fugiat nulla pariatur.</p>
    <p class="abs tiny center" style="left:195px;top:100px;width:60px;margin:0">dolor sit amet, consectetur adipiscing elit, sed do eiusmod tempor incididunt ut labore et dolore magna aliqua. Ut enim ad minim veniam, quis nostrud exercitation ullamco laboris nisi ut aliquip ex ea fugiat nulla pariatur.</p>
    <div class="mini-logo"><i></i>Vast KELP</div>
    <div class="foot"></div>
  </section>

  <!-- Services -->
  <section class="slide">
    <div class="slide-title">Our services</div>
    <div class="service" style="left:43px">
      <div class="top" style="background:var(--green)">
        <svg width="16" height="16" viewBox="0 0 16 16"><path d="M8 1l7 7-3 3-2-1v2L8 15 1 8l3-3h2V3z" fill="#fff"/></svg>
      </div>
      <div class="bottom">Dolor sit amet, consectetur adipiscing elit, sed do eiusmod tempor incididunt ut labore et dolore magna aliqua.</div>
    </div>
    <div class="service" style="left:113px">
      <div class="top" style="background:#8d8d8d">
        <svg width="16" height="16" viewBox="0 0 16 16"><circle cx="8" cy="9" r="6" fill="none" stroke="#fff" stroke-width="1.6"/><rect x="6.5" y="1" width="3" height="1.6" fill="#fff"/><path d="M8 9V5.5" stroke="#fff" stroke-width="1.4"/></svg>
      </div>
      <div class="bottom">Dolor sit amet, consectetur adipiscing elit, sed do eiusmod tempor incididunt ut labore et dolore magna aliqua.</div>
    </div>
    <div class="service" style="left:182px">
      <div class="top" style="background:var(--green)">
        <svg width="16" height="16" viewBox="0 0 16 16"><rect x="2" y="9" width="3" height="5" fill="#fff"/><rect x="6.5" y="6" width="3" height="8" fill="#fff"/><rect x="11" y="7" width="3" height="7" fill="#fff"/><path d="M3 6l4-3 3 2 4-3" stroke="#fff" stroke-width="1.2" fill="none"/></svg>
      </div>
      <div class="bottom">Dolor sit amet, consectetur adipiscing elit, sed do eiusmod tempor incididunt ut labore et dolore magna aliqua.</div>
    </div>
    <div class="mini-logo"><i></i>Vast KELP</div>
    <div class="foot"></div>
  </section>

  <!-- Team -->
  <section class="slide">
    <div class="slide-title">Our team</div>
    <div class="member" style="left:27px">
      <div class="avatar" role="img" aria-label="Portrait of the president"></div>
      <h4>JONATHAN DOE</h4><small>President</small>
      <p class="tiny center" style="margin:0">dolor sit amet, consectetur adipiscing elit, sed do eiusmod tempor incididunt ut labore et dolore magna aliqua. Ut enim ad minim veniam, quis nostrud exercitation ullamco laboris nisi ut aliquip ex ea fugiat nulla pariatur.</p>
    </div>
    <div class="member" style="left:113px">
      <div class="avatar" role="img" aria-label="Portrait of the CEO and founder"></div>
      <h4>MELANIE DOE</h4><small>CEO / Founder</small>
      <p class="tiny center" style="margin:0">dolor sit amet, consectetur adipiscing elit, sed do eiusmod tempor incididunt ut labore et dolore magna aliqua. Ut enim ad minim veniam, quis nostrud exercitation ullamco laboris nisi ut aliquip ex ea fugiat nulla pariatur.</p>
    </div>
    <div class="member" style="left:205px">
      <div class="avatar" role="img" aria-label="Portrait of the vice president"></div>
      <h4>NATALIE DOE</h4><small>Vice President</small>
      <p class="tiny center" style="margin:0">dolor sit amet, consectetur adipiscing elit, sed do eiusmod tempor incididunt ut labore et dolore magna aliqua. Ut enim ad minim veniam, quis nostrud exercitation ullamco laboris nisi ut aliquip ex ea fugiat nulla pariatur.</p>
    </div>
    <div class="mini-logo"><i></i>Vast KELP</div>
    <div class="foot"></div>
  </section>

  <!-- Table -->
  <section class="slide">
    <div class="slide-title">Our table</div>
    <table class="data-table">
      <caption>Growth &amp; Income Investments</caption>
      <tr><td>Calm Harbor</td><td>Sharon</td><td>IRA</td><td>$</td><td class="num">176,446.44</td></tr>
      <tr><td>Orbit Asset Management</td><td>Trust</td><td>NQ</td><td>$</td><td class="num">211,814.62</td></tr>
      <tr><td>Steady Portfolio</td><td>Trust</td><td>NQ</td><td>$</td><td class="num">177,653.59</td></tr>
      <tr><td>Wellstead Care Trust</td><td>Ken</td><td>IRA</td><td>$</td><td class="num">269,724.35</td></tr>
      <tr><td>Silver</td><td>Ken</td><td>IRA</td><td>$</td><td class="num">37,766.33</td></tr>
      <tr><td>Larkfield</td><td>Ken</td><td>IRA</td><td>$</td><td class="num">47,864.15</td></tr>
      <tr><td>Larkfield</td><td>Sharon</td><td>IRA</td><td>$</td><td class="num">10,746.27</td></tr>
      <tr><td>Northgate</td><td>Ken</td><td>IRA</td><td>$</td><td class="num">77,123.47</td></tr>
      <tr><td>Prism Capital</td><td>Ken</td><td>IRA</td><td>$</td><td class="num">58,643.79</td></tr>
      <tr><td>Prism Capital</td><td>Sharon</td><td>IRA</td><td>$</td><td class="num">80,250.22</td></tr>
      <tr class="total"><td>Total Growth &amp; Income Investments</td><td></td><td></td><td>$</td><td class="num">1,147,583.83</td></tr>
    </table>
    <div class="mini-logo"><i></i>Vast KELP</div>
    <div class="foot"></div>
  </section>

  <!-- Partners -->
  <section class="slide">
    <div class="slide-title">Our partners</div>
    <div class="abs partner-box">
      <span class="badge" style="background:#d9302c"></span>
      <span class="badge" style="background:#2f6ab0"></span>
      <span class="badge" style="background:#1f3f7a"></span>
      <span class="badge" style="background:#1d2a4e;width:10px;height:10px"></span>
      <span class="badge" style="background:#7aa7da"></span>
      <span class="badge" style="background:#c2262e"></span>
      <span class="badge" style="background:#2f8c7a"></span>
      <span class="badge" style="background:#d62f2f;width:12px"></span>
      <span class="badge" style="background:#2a3e8a"></span>
      <span class="badge" style="background:#f08a5d"></span>
      <span class="badge" style="background:#6a9f3a"></span>
      <span class="badge" style="background:#e7c04e;width:10px;height:10px;border-radius:50%"></span>
      <span class="badge" style="background:#2454a0"></span>
      <span class="badge" style="background:#9aa3ad"></span>
      <span class="badge" style="background:#244c9c"></span>
      <span class="badge" style="background:#3a6fb0;width:18px"></span>
    </div>
    <div class="mini-logo"><i></i>Vast KELP</div>
    <div class="foot"></div>
  </section>

  <!-- Image with text -->
  <section class="slide">
    <div class="abs imgtext-panel">
      <h3>IMAGE TEXT</h3>
      <p class="tiny" style="margin:0">Lorem ipsum dolor sit amet, consectetur adipiscing elit, sed do eiusmod tempor incididunt ut labore et dolore magna aliqua. Ut enim ad minim veniam, quis nostrud exercitation ullamco laboris nisi ut aliquip ex ea commodo consequat. Duis aute irure dolor in reprehenderit in voluptate velit esse cillum dolore eu fugiat nulla pariatur.</p>
    </div>
    <div class="img-fill imgtext-photo" role="img" aria-label="Test tubes with blue liquid and a pipette"></div>
    <div class="mini-logo" style="color:#fff"><i style="background:#fff"></i>Vast KELP</div>
  </section>

  <!-- Section divider -->
  <section class="slide">
    <div class="img-fill section-bg" role="img" aria-label="Green microscopic cells and virus particles"></div>
    <div class="abs section-mark">i</div>
    <div class="abs section-rule"></div>
    <div class="abs section-title">SECTION TITLE</div>
  </section>

  <!-- Contact -->
  <section class="slide">
    <div class="abs contact-top"></div>
    <div class="abs brand" style="left:30px;top:31px;font-size:12px"><i style="width:8px;height:8px"></i>Vast KELP</div>
    <div class="img-fill contact-map" role="img" aria-label="Street map with waterways showing the office location"></div>
    <svg class="abs" style="left:203px;top:78px" width="8" height="11" viewBox="0 0 8 11"><path d="M4 0a4 4 0 0 1 4 4c0 3-4 7-4 7S0 7 0 4a4 4 0 0 1 4-4z" fill="#d83a2a"/><circle cx="4" cy="4" r="1.4" fill="#fff"/></svg>
    <div class="abs contact-bar">
      <span><i></i>412 Harbor Reach Way Ste 90</span>
      <span><i></i>hello@vastkelp.com</span>
      <span><i></i>www.vastkelp.com</span>
    </div>
  </section>

</main>
</body>
</html>
```